UI Improvement for FlorvaLink app

We are looking for a talented UI/UX designer to REFINE and enhance the visual design of our mobile application, FlorvaLink. The app is fully functional, but we need a designer to improve its aesthetics by specifying design elements such as fonts, colors, spacing, and component styles.
Your task will be to analyze the CURRENT UI and provide detailed design specifications that will make the app more visually appealing, modern, and user-friendly.
TODO:
Review the existing FlorvaLink app design (see attachments) and identify areas for visual improvement.
Provide a detailed UI style guide, including:
Typography (font choices, sizes, and weights)
Color palette (primary, secondary, and accent colors)
Component styling (buttons, forms, icons, and interactive elements)
Spacing and layout guidelines (margins, paddings, and alignment)
Ensure the design remains clean, modern, and professional while maintaining usability and accessibility.
Provide design mockups or visual examples (if possible) to illustrate the proposed changes.
Deliverables:
A UI Style Guide (PDF or Figma file) with specifications on fonts, colors, spacing, and UI components.
Optionally, before/after mockups or examples demonstrating the improvements.
Ideal Designer:
Strong experience in mobile UI/UX design.
Understanding of modern design trends and best practices.
Ability to communicate design choices clearly for easy developer implementation.
I have attached 7 images showcasing the main UI screens used in the FlorvaLink app. These screens need visual enhancements to improve their overall look and user experience.
The images represent the current design in three key modes:
LIST Mode – Displays data in a structured list format.
READ Mode – Shows detailed information when a user selects an item.
ADD/EDIT Mode – Allows users to input or modify information.
Additionally, there is a ‘MORE’ page, which serves as a menu listing other features of the application.
Task Objective:
Please refine and improve these UIs to create a more modern, visually appealing, and user-friendly experience. Focus on typography, colors, spacing, and component styling to ensure a cohesive and polished design.
Look and feel
Each slider illustrates characteristics of the customer's brand and the style your logo design should communicate.

```html
<!DOCTYPE html>
<html lang="en">
<head>
<meta charset="utf-8">
<title>FlorvaLink – Screens</title>
<link href="https://fonts.googleapis.com/css2?family=Roboto:wght@400;500;700&display=swap" rel="stylesheet">
<style>
:root{
  --canvas:#1e1e1e;
  --screen:#eef0f3;
  --card:#ffffff;
  --ink:#1f1f1f;
  --muted:#9a9a9a;
  --line:#c9ccd1;
  --blue:#1a7cf5;
  --red:#e5384f;
  --owner:#c9f3f3;
  --pilot:#fbefc4;
  --qualified:#c8f1c4;
  --yellow:#f5d328;
  --cyan:#3de8ec;
  --green:#2fe83a;
  --icon:#b4b7bd;
  --avatar:#e4e6e9;
}
*{box-sizing:border-box;margin:0;padding:0}
html,body{width:786px;height:1200px;overflow:hidden;background:var(--canvas);font-family:'Roboto',sans-serif;color:var(--ink)}
.board{position:absolute;left:0;top:0;width:1356px;height:2071px;transform:scale(0.5796);transform-origin:0 0}
.screen{position:absolute;width:412px;height:917px;background:var(--screen);overflow:hidden}
.screen *{position:absolute}
.hdr{left:0;top:0;width:412px;height:62px;text-align:center}
.hdr .sub{left:0;width:412px;top:14px;font-size:12px;color:#666;font-weight:500}
.hdr .ttl{left:0;width:412px;top:30px;font-size:16px}
.hdr .solo{left:0;width:412px;top:22px;font-size:16px}
.back{left:16px;top:22px}
.dots{font-size:18px;letter-spacing:1px;color:#444;line-height:1}
.card{background:var(--card)}
.field{border:1px solid var(--line);border-radius:2px;background:#fff}
.field.focus{border-color:#2f6fd8}
.field .lbl{top:-8px;left:12px;background:#fff;padding:0 6px;font-size:12px;font-weight:500;line-height:14px;white-space:nowrap}
.field.focus .lbl{color:var(--blue);font-weight:700}
.field .ph{left:16px;top:15px;font-size:14px;color:var(--muted);white-space:nowrap}
.field .val{left:40px;top:14px;font-size:14px;white-space:nowrap}
.field .ico{left:16px;top:17px}
.req{font-size:11px;color:var(--red);font-style:italic}
.caret{width:0;height:0;border-left:6px solid transparent;border-right:6px solid transparent;border-top:6px solid #999}
.search{border:1px solid var(--line);border-radius:16px;background:#fff;height:32px}
.search span{left:38px;top:7px;font-size:14px;color:var(--muted)}
.search svg{left:14px;top:7px}
.filter{background:var(--blue);color:#fff;height:32px;border-radius:2px;font-size:13px}
.filter span{left:43px;top:8px}
.filter svg{left:14px;top:7px}
.item{left:6px;width:400px;height:108px;background:var(--card)}
.avatar{left:15px;top:20px;width:68px;height:68px;background:var(--avatar);border-radius:3px}
.name{left:92px;top:26px;font-size:16px;font-weight:700;color:var(--blue);white-space:nowrap}
.chip{height:24px;border-radius:12px;font-size:12px;line-height:24px;padding:0 14px;white-space:nowrap;position:absolute}
.chip.owner{background:var(--owner)}
.chip.pilot{background:var(--pilot)}
.chip.qual{background:var(--qualified)}
.chip.plain{background:#fff;border:1px solid var(--line);line-height:22px}
.tag{height:30px;border:1px solid var(--line);border-radius:15px;background:#fff;font-size:14px;font-weight:400;line-height:28px;padding:0 12px 0 36px;white-space:nowrap}
.tag svg{left:12px;top:7px}
.tag.small{height:24px;line-height:22px;font-size:12px;padding:0 12px 0 36px}
.tag.small svg{top:4px}
.tagrow{display:flex;gap:8px}
.tagrow .tag{position:static;padding:0 12px;height:28px;line-height:26px}
.row{left:6px;width:400px;height:38px;background:var(--card)}
.row svg{left:14px;top:11px}
.row span{left:42px;top:11px;font-size:13px}
.section{left:6px;width:400px;background:var(--card)}
.section .bar{left:0;top:0;width:400px;height:4px}
.section .head{left:44px;top:22px;font-size:13px;font-weight:500}
.section .hico{left:14px;top:18px}
.section .coll{right:14px;top:22px;font-size:12px;color:var(--muted)}
.section .coll i{position:relative;display:inline-block;margin-left:8px;top:-2px;border-left:5px solid transparent;border-right:5px solid transparent;border-top:5px solid #999}
.tabs{left:0;width:412px;height:82px;background:#fff;bottom:0}
.tab{top:14px;width:78px;text-align:center}
.tab svg{left:25px;top:0}
.tab span{left:0;width:78px;top:38px;font-size:12px;color:var(--muted)}
.tab.on span{color:var(--blue);font-weight:700}
.menu{left:6px;width:400px;height:48px;background:var(--card)}
.menu svg{left:16px;top:13px}
.menu span{left:50px;top:15px;font-size:13px}
.link{font-size:13px}
</style>
</head>
<body>
<svg width="0" height="0" style="position:absolute">
  <defs>
    <symbol id="i-person" viewBox="0 0 24 24"><circle cx="12" cy="7" r="5"/><path d="M2 23c0-6 4.5-9 10-9s10 3 10 9z"/></symbol>
    <symbol id="i-pilot" viewBox="0 0 24 24"><path d="M5 3h14l-2 4H7z"/><circle cx="12" cy="11" r="4"/><path d="M3 23c0-5 4-8 9-8s9 3 9 8z"/></symbol>
    <symbol id="i-plane" viewBox="0 0 24 24"><path d="M22 12c0-1-1-1.5-2-1.5h-5L10 3H8l2.5 7.5H5L3 8H1.5l1.2 4-1.2 4H3l2-2.5h5.5L8 21h2l5-7.5h5c1 0 2-.5 2-1.5z"/></symbol>
    <symbol id="i-hand" viewBox="0 0 24 24"><path d="M8 2h2v10h1V4h2v8h1V5h2v9l2-3h2l-3 8c-1 3-3 4-6 4-4 0-5-2-5-5V2z"/></symbol>
    <symbol id="i-more" viewBox="0 0 24 24"><circle cx="4" cy="12" r="2.5"/><circle cx="12" cy="12" r="2.5"/><circle cx="20" cy="12" r="2.5"/></symbol>
    <symbol id="i-tag" viewBox="0 0 24 24"><path d="M2 12 12 2h9v9L11 21z"/></symbol>
    <symbol id="i-case" viewBox="0 0 24 24"><path d="M8 5V3h8v2h6v15H2V5z"/></symbol>
    <symbol id="i-doc" viewBox="0 0 24 24"><path d="M4 3h16v18H4z"/></symbol>
    <symbol id="i-cal" viewBox="0 0 24 24"><path d="M2 2h20v14l-6 6H2z"/></symbol>
    <symbol id="i-check" viewBox="0 0 24 24"><circle cx="12" cy="12" r="10"/><path d="m7 12 3.5 3.5L17 9" stroke="#fff" stroke-width="2.5" fill="none"/></symbol>
    <symbol id="i-takeoff" viewBox="0 0 24 24"><path d="M2 20h20v2H2zM3 15l17-5c1-.3 2 .5 1.5 1.3L6 16l-3-3 2-.5z"/></symbol>
    <symbol id="i-pin" viewBox="0 0 24 24"><path d="M12 2a7 7 0 0 0-7 7c0 5 7 13 7 13s7-8 7-13a7 7 0 0 0-7-7zm0 9.5A2.5 2.5 0 1 1 12 6.5a2.5 2.5 0 0 1 0 5z"/></symbol>
    <symbol id="i-phone" viewBox="0 0 24 24"><path d="M6 2h4l1 5-2.5 2a12 12 0 0 0 6.5 6.5L17 13l5 1v4c0 2-1 3-3 3C10 21 3 14 3 5c0-2 1-3 3-3z"/></symbol>
    <symbol id="i-people" viewBox="0 0 24 24"><circle cx="8" cy="5" r="3"/><circle cx="16" cy="5" r="3"/><path d="M3 22V11h10v11zM11 22V11h10v11z"/></symbol>
    <symbol id="i-users" viewBox="0 0 24 24"><circle cx="12" cy="8" r="4"/><circle cx="4.5" cy="9" r="3"/><circle cx="19.5" cy="9" r="3"/><path d="M5 20c0-4 3-6 7-6s7 2 7 6zM0 18c0-3 2-5 5-5l-1 5zM24 18c0-3-2-5-5-5l1 5z"/></symbol>
    <symbol id="i-home" viewBox="0 0 24 24"><path d="M12 2 1 12h3v10h6v-6h4v6h6V12h3z"/></symbol>
    <symbol id="i-map" viewBox="0 0 24 24"><path d="M1 4l7-2 8 3 7-2v17l-7 2-8-3-7 2z"/></symbol>
    <symbol id="i-gift" viewBox="0 0 24 24"><path d="M2 7h20v5H2zM4 12h16v10H4zM12 7c-2-5-7-4-5-1zM12 7c2-5 7-4 5-1z"/></symbol>
    <symbol id="i-wrench" viewBox="0 0 24 24"><path d="M3 19 14 8a5 5 0 0 1 7-6l-3 3 1 3 3 1 3-3a5 5 0 0 1-6 7L8 24z"/></symbol>
    <symbol id="i-gear" viewBox="0 0 24 24"><path d="M10 1h4l1 3 3 1.5 3-1.5 2 3.5-2 2.5v3l2 2.5-2 3.5-3-1.5L15 20l-1 3h-4l-1-3-3-1.5L3 20l-2-3.5 2-2.5v-3L1 8.5 3 5l3 1.5L9 4zM12 8a4 4 0 1 0 0 8 4 4 0 0 0 0-8z"/></symbol>
    <symbol id="i-plus" viewBox="0 0 24 24"><circle cx="12" cy="12" r="10" fill="none" stroke="currentColor" stroke-width="1.6"/><path d="M12 7v10M7 12h10" stroke="currentColor" stroke-width="1.6"/></symbol>
    <symbol id="i-back" viewBox="0 0 24 24"><path d="M21 12H4M11 5l-7 7 7 7" fill="none" stroke="currentColor" stroke-width="2.2"/></symbol>
    <symbol id="i-search" viewBox="0 0 24 24"><circle cx="10" cy="10" r="7" fill="none" stroke="currentColor" stroke-width="2"/><path d="m15 15 7 7" stroke="currentColor" stroke-width="2"/></symbol>
    <symbol id="i-sliders" viewBox="0 0 24 24"><path d="M5 2v20M12 2v20M19 2v20" stroke="currentColor" stroke-width="1.6"/><rect x="2.5" y="13" width="5" height="4" fill="currentColor"/><rect x="9.5" y="5" width="5" height="4" fill="currentColor"/><rect x="16.5" y="11" width="5" height="4" fill="currentColor"/></symbol>
    <symbol id="i-star" viewBox="0 0 24 24"><path d="m12 2 3 7 7.5.6-5.7 5 1.8 7.4L12 18l-6.6 4 1.8-7.4-5.7-5L9 9z"/></symbol>
  </defs>
</svg>

<div class="board">

<!-- ADD CONTACT -->
<section class="screen" style="left:30px;top:30px">
  <header class="hdr">
    <svg class="back" width="22" height="22" style="color:#222"><use href="#i-back"/></svg>
    <span class="sub">Add</span><span class="ttl">Contact</span>
    <span style="left:330px;top:22px;font-size:16px;font-weight:700;color:var(--blue)">Save</span>
    <span class="dots" style="left:378px;top:22px">···</span>
  </header>
  <div class="card" style="left:6px;top:64px;width:400px;height:324px"></div>
  <div class="field focus" style="left:18px;top:93px;width:340px;height:49px"><span class="lbl">Business Name</span><span class="ph">Enter Business Name</span></div>
  <span class="dots" style="left:378px;top:110px">···</span>
  <div class="field" style="left:18px;top:172px;width:378px;height:49px"><span class="lbl">First Name</span><span class="ph">Enter First Name</span></div>
  <div class="field" style="left:18px;top:245px;width:378px;height:49px"><span class="lbl">Middle Name</span><span class="ph">Enter Middle Name</span></div>
  <div class="field" style="left:18px;top:318px;width:378px;height:49px"><span class="lbl">Last Name</span><span class="ph">Enter Last Name</span></div>

  <div class="card" style="left:6px;top:404px;width:400px;height:440px"></div>
  <div class="field" style="left:17px;top:433px;width:340px;height:49px"><span class="lbl">Address Label Tag</span><span class="ph">Select Address Label Tag</span></div>
  <span class="dots" style="left:378px;top:453px">···</span>
  <span class="req" style="left:17px;top:485px">*&nbsp; Required</span>
  <div class="field" style="left:17px;top:523px;width:378px;height:49px"><span class="lbl">Address Line 1</span><span class="ph">Street Address</span></div>
  <span class="req" style="left:17px;top:575px">*&nbsp; Required</span>
  <div class="field" style="left:17px;top:613px;width:378px;height:49px"><span class="lbl">Address Line 2</span><span class="ph">Apartment, Suite, Building, etc. (optional)</span></div>
  <div class="field" style="left:18px;top:686px;width:377px;height:49px"><span class="lbl">City</span><span class="ph">Select City</span><i class="caret" style="right:14px;top:21px"></i></div>
  <div class="field" style="left:18px;top:759px;width:183px;height:49px"><span class="lbl">State</span><span class="ph">Select State</span><i class="caret" style="right:14px;top:21px"></i></div>
  <div class="field" style="left:211px;top:759px;width:184px;height:49px"><span class="lbl">ZIP Code</span><span class="ph">Enter ZIP Code</span></div>

  <nav class="tabs" style="top:835px">
    <div class="tab on" style="left:11px"><svg width="28" height="28" fill="var(--blue)"><use href="#i-person"/></svg><span>Contact</span></div>
    <div class="tab" style="left:89px"><svg width="28" height="28" fill="var(--icon)"><use href="#i-tag"/></svg><span>Quote</span></div>
    <div class="tab" style="left:167px"><svg width="28" height="28" fill="var(--icon)"><use href="#i-case"/></svg><span>Work Order</span></div>
    <div class="tab" style="left:245px"><svg width="28" height="28" fill="var(--icon)"><use href="#i-doc"/></svg><span>Invoice</span></div>
    <div class="tab" style="left:323px"><svg width="28" height="28" fill="var(--icon)"><use href="#i-more"/></svg><span>More</span></div>
  </nav>
</section>

<!-- CONTACTS LIST -->
<section class="screen" style="left:472px;top:30px">
  <header class="hdr">
    <span class="solo">Contacts</span>
    <span style="left:348px;top:16px;font-size:26px;font-weight:300;color:#333">+</span>
    <span class="dots" style="left:378px;top:22px">···</span>
  </header>
  <div class="card" style="left:0;top:62px;width:412px;height:70px"></div>
  <div class="search" style="left:18px;top:83px;width:274px"><svg width="18" height="18" style="color:#888"><use href="#i-search"/></svg><span>Search</span></div>
  <div class="filter" style="left:304px;top:83px;width:90px"><svg width="18" height="18" style="color:#fff"><use href="#i-sliders"/></svg><span>Filter</span></div>

  <article class="item" style="top:141px"><div class="avatar" role="img" aria-label="Contact photo"></div><span class="name">Ashford, Colin</span>
    <span class="chip owner" style="left:92px;top:56px">Aircraft Owner</span><span class="chip plain" style="left:205px;top:56px">Enthusiast</span><span class="chip plain" style="left:299px;top:56px">Flight Support</span></article>
  <article class="item" style="top:255px"><div class="avatar" role="img" aria-label="Contact photo"></div><span class="name">Avery, Clark, Blake</span>
    <span class="chip owner" style="left:92px;top:56px">Aircraft Owner</span><span class="chip pilot" style="left:205px;top:56px">Pilot</span><span class="chip qual" style="left:266px;top:56px">Qualified Pilot</span></article>
  <article class="item" style="top:369px"><div class="avatar" role="img" aria-label="Contact photo"></div><span class="name">Barlow, Reid</span>
    <span class="chip owner" style="left:92px;top:56px">Aircraft Owner</span><span class="chip pilot" style="left:205px;top:56px">Pilot</span><span class="chip qual" style="left:266px;top:56px">Qualified Pilot</span></article>
  <article class="item" style="top:483px"><div class="avatar" role="img" aria-label="Contact photo"></div><span class="name">Brennick, Alan</span>
    <span class="chip owner" style="left:92px;top:56px">Aircraft Owner</span><span class="chip pilot" style="left:205px;top:56px">Pilot</span><span class="chip qual" style="left:266px;top:56px">Qualified Pilot</span></article>
  <article class="item" style="top:597px"><div class="avatar" role="img" aria-label="Contact photo"></div><span class="name">Corwin, Ada, Selene</span>
    <span class="chip pilot" style="left:92px;top:56px">Pilot</span></article>
  <article class="item" style="top:711px"><div class="avatar" role="img" aria-label="Contact photo"></div><span class="name">Cruz Moreno, Hugo, Yaretzi</span>
    <span class="chip pilot" style="left:92px;top:56px">Pilot</span></article>
  <article class="item" style="top:825px"></article>

  <nav class="tabs" style="top:835px">
    <div class="tab on" style="left:11px"><svg width="28" height="28" fill="var(--blue)"><use href="#i-person"/></svg><span>Contact</span></div>
    <div class="tab" style="left:89px"><svg width="28" height="28" fill="var(--icon)"><use href="#i-pilot"/></svg><span>Pilot</span></div>
    <div class="tab" style="left:167px"><svg width="28" height="28" fill="var(--icon)"><use href="#i-plane"/></svg><span>Plane</span></div>
    <div class="tab" style="left:245px"><svg width="28" height="28" fill="var(--icon)"><use href="#i-hand"/></svg><span>Flt Request</span></div>
    <div class="tab" style="left:323px"><svg width="28" height="28" fill="var(--icon)"><use href="#i-more"/></svg><span>More</span></div>
  </nav>
</section>

<!-- CONTACT DETAIL -->
<section class="screen" style="left:914px;top:30px;height:1064px">
  <header class="hdr">
    <svg class="back" width="22" height="22" style="color:#222"><use href="#i-back"/></svg>
    <span class="sub">Contact</span><span class="ttl">Ashford, Colin</span>
    <span class="dots" style="left:378px;top:22px">···</span>
  </header>
  <div class="row" style="top:63px"><svg width="16" height="16" style="color:var(--blue)"><use href="#i-plus"/></svg><span>Add Email</span></div>
  <div class="row" style="top:110px"><svg width="16" height="16" style="color:var(--blue)"><use href="#i-plus"/></svg><span>Add Social Media</span></div>
  <div class="row" style="top:157px"><svg width="16" height="16" style="color:var(--blue)"><use href="#i-plus"/></svg><span>Add Emergency Contact</span></div>
  <div class="row" style="top:205px"><svg width="16" height="16" style="color:var(--blue)"><use href="#i-plus"/></svg><span>Add Personal Information</span></div>
  <div class="row" style="top:252px"><svg width="16" height="16" style="color:var(--blue)"><use href="#i-plus"/></svg><span>Add Work Info</span></div>
  <div class="row" style="top:300px"><svg width="16" height="16" style="color:var(--blue)"><use href="#i-plus"/></svg><span>Add Skills/Talents</span></div>
  <div class="row" style="top:347px"><svg width="16" height="16" style="color:var(--blue)"><use href="#i-plus"/></svg><span>Add Resources</span></div>

  <div class="section" style="top:395px;height:160px">
    <div class="bar" style="background:var(--yellow)"></div>
    <svg class="hico" width="20" height="20" fill="var(--icon)"><use href="#i-pilot"/></svg>
    <span class="head">Pilots</span><span class="coll">Collapse<i></i></span>
    <span class="tag" style="left:15px;top:62px"><svg width="16" height="16" fill="var(--icon)"><use href="#i-pilot"/></svg>Ashford</span>
    <span class="tag" style="left:128px;top:62px"><svg width="16" height="16" fill="var(--icon)"><use href="#i-pilot"/></svg>Colin</span>
    <span class="tag" style="left:223px;top:62px"><svg width="16" height="16" fill="var(--icon)"><use href="#i-check"/></svg>3647946</span>
    <span class="tag" style="left:15px;top:104px"><svg width="16" height="16" fill="var(--icon)"><use href="#i-cal"/></svg>10/31/2023</span>
  </div>

  <div class="section" style="top:565px;height:240px">
    <div class="bar" style="background:var(--cyan)"></div>
    <svg class="hico" width="20" height="20" fill="var(--icon)"><use href="#i-pilot"/></svg>
    <span class="head">Aircraft Owner</span><span class="coll">Collapse<i></i></span>
    <span class="tag" style="left:15px;top:62px"><svg width="16" height="16" fill="var(--icon)"><use href="#i-pilot"/></svg>Ashford</span>
    <span class="tag" style="left:128px;top:62px"><svg width="16" height="16" fill="var(--icon)"><use href="#i-pilot"/></svg>Colin</span>
    <span class="tag" style="left:223px;top:62px"><svg width="16" height="16" fill="var(--icon)"><use href="#i-takeoff"/></svg>Aerolux</span>
    <span class="tag" style="left:15px;top:104px"><svg width="16" height="16" fill="var(--icon)"><use href="#i-plane"/></svg>A20X</span>
    <span class="tag" style="left:109px;top:104px"><svg width="16" height="16" fill="var(--icon)"><use href="#i-takeoff"/></svg>Aerolux Aircraft Co</span>
    <span class="tag" style="left:15px;top:146px"><svg width="16" height="16" fill="var(--icon)"><use href="#i-plane"/></svg>Single Engine</span>
    <span class="tag" style="left:162px;top:146px"><svg width="16" height="16" fill="var(--icon)"><use href="#i-plane"/></svg>1100</span>
    <div style="left:14px;top:193px;width:372px;height:1px;background:#e2e4e7"></div>
    <svg width="16" height="16" style="left:14px;top:208px;color:var(--blue)"><use href="#i-plus"/></svg>
    <span class="link" style="left:42px;top:208px">Add Aircraft Owner</span>
  </div>

  <div class="section" style="top:813px;height:200px">
    <div class="bar" style="background:var(--green)"></div>
    <svg class="hico" width="20" height="20" fill="var(--icon)"><use href="#i-person"/></svg>
    <span class="head">Aircraft Owner</span><span class="coll">Collapse<i></i></span>
    <span class="tag" style="left:15px;top:62px"><svg width="16" height="16" fill="var(--icon)"><use href="#i-pilot"/></svg>Ashford</span>
    <span class="tag" style="left:128px;top:62px"><svg width="16" height="16" fill="var(--icon)"><use href="#i-pilot"/></svg>Colin</span>
    <span class="tag" style="left:223px;top:62px"><svg width="16" height="16" fill="var(--icon)"><use href="#i-takeoff"/></svg>Aerolux</span>
    <span class="tag" style="left:15px;top:104px"><svg width="16" height="16" fill="var(--icon)"><use href="#i-plane"/></svg>A20X</span>
    <span class="tag" style="left:109px;top:104px"><svg width="16" height="16" fill="var(--icon)"><use href="#i-takeoff"/></svg>Aerolux Aircraft Co</span>
    <span class="tag" style="left:15px;top:146px"><svg width="16" height="16" fill="var(--icon)"><use href="#i-plane"/></svg>Single Engine</span>
    <span class="tag" style="left:162px;top:146px"><svg width="16" height="16" fill="var(--icon)"><use href="#i-plane"/></svg>1100</span>
  </div>

  <nav class="tabs" style="top:982px">
    <div class="tab on" style="left:11px"><svg width="28" height="28" fill="var(--blue)"><use href="#i-person"/></svg><span>Contact</span></div>
    <div class="tab" style="left:89px"><svg width="28" height="28" fill="var(--icon)"><use href="#i-pilot"/></svg><span>Pilot</span></div>
    <div class="tab" style="left:167px"><svg width="28" height="28" fill="var(--icon)"><use href="#i-plane"/></svg><span>Plane</span></div>
    <div class="tab" style="left:245px"><svg width="28" height="28" fill="var(--icon)"><use href="#i-hand"/></svg><span>Flt Request</span></div>
    <div class="tab" style="left:323px"><svg width="28" height="28" fill="var(--icon)"><use href="#i-more"/></svg><span>More</span></div>
  </nav>
</section>

<!-- PILOTS LIST -->
<section class="screen" style="left:30px;top:1124px">
  <header class="hdr">
    <span class="solo">Pilots</span>
    <span style="left:348px;top:16px;font-size:26px;font-weight:300;color:#333">+</span>
    <span class="dots" style="left:378px;top:22px">···</span>
  </header>
  <div class="card" style="left:0;top:62px;width:412px;height:70px"></div>
  <div class="search" style="left:18px;top:83px;width:274px"><svg width="18" height="18" style="color:#888"><use href="#i-search"/></svg><span>Search</span></div>
  <div class="filter" style="left:304px;top:83px;width:90px"><svg width="18" height="18" style="color:#fff"><use href="#i-sliders"/></svg><span>Filter</span></div>

  <article class="item" style="top:141px"><div class="avatar" role="img" aria-label="Pilot photo"></div><span class="name">Avery, Clark, Blake</span>
    <span class="tag small" style="left:284px;top:22px"><svg width="16" height="16" fill="var(--icon)"><use href="#i-check"/></svg>3182133</span>
    <span class="tag small" style="left:92px;top:62px"><svg width="14" height="14" fill="var(--icon)"><use href="#i-cal"/></svg>09/20/24</span></article>
  <article class="item" style="top:255px"><div class="avatar" role="img" aria-label="Pilot photo"></div><span class="name">Barlow, Reid</span>
    <span class="tag small" style="left:284px;top:22px"><svg width="16" height="16" fill="var(--icon)"><use href="#i-check"/></svg>4467155</span>
    <span class="tag small" style="left:92px;top:62px"><svg width="14" height="14" fill="var(--icon)"><use href="#i-cal"/></svg>02/28/25</span></article>
  <article class="item" style="top:369px"><div class="avatar" role="img" aria-label="Pilot photo"></div><span class="name">Brennick, Alan</span>
    <span class="tag small" style="left:284px;top:22px"><svg width="16" height="16" fill="var(--icon)"><use href="#i-check"/></svg>2663187</span>
    <span class="tag small" style="left:92px;top:62px"><svg width="14" height="14" fill="var(--icon)"><use href="#i-cal"/></svg>10/30/24</span></article>
  <article class="item" style="top:483px"><div class="avatar" role="img" aria-label="Pilot photo"></div><span class="name">Corwin, Ada, Selene</span>
    <span class="tag small" style="left:284px;top:22px"><svg width="16" height="16" fill="var(--icon)"><use href="#i-check"/></svg>4360575</span>
    <span class="tag small" style="left:92px;top:62px"><svg width="14" height="14" fill="var(--icon)"><use href="#i-cal"/></svg>03/30/25</span></article>
  <article class="item" style="top:597px"><div class="avatar" role="img" aria-label="Pilot photo"></div><span class="name" style="font-size:12px;top:28px">Cruz Moreno, Hugo, Yaretzi</span>
    <span class="tag small" style="left:284px;top:22px"><svg width="16" height="16" fill="var(--icon)"><use href="#i-check"/></svg>0000000</span>
    <span class="tag small" style="left:92px;top:62px"><svg width="14" height="14" fill="var(--icon)"><use href="#i-cal"/></svg>00/00/00</span></article>
  <article class="item" style="top:711px"><div class="avatar" role="img" aria-label="Pilot photo"></div><span class="name">Garner, Cole</span>
    <span class="tag small" style="left:291px;top:22px"><svg width="16" height="16" fill="var(--icon)"><use href="#i-check"/></svg>342819</span>
    <span class="tag small" style="left:92px;top:62px"><svg width="14" height="14" fill="var(--icon)"><use href="#i-cal"/></svg>02/28/25</span></article>
  <article class="item" style="top:825px"></article>

  <nav class="tabs" style="top:835px">
    <div class="tab" style="left:11px"><svg width="28" height="28" fill="var(--icon)"><use href="#i-person"/></svg><span>Contact</span></div>
    <div class="tab on" style="left:89px"><svg width="28" height="28" fill="var(--blue)"><use href="#i-pilot"/></svg><span>Pilot</span></div>
    <div class="tab" style="left:167px"><svg width="28" height="28" fill="var(--icon)"><use href="#i-plane"/></svg><span>Plane</span></div>
    <div class="tab" style="left:245px"><svg width="28" height="28" fill="var(--icon)"><use href="#i-hand"/></svg><span>Flt Request</span></div>
    <div class="tab" style="left:323px"><svg width="28" height="28" fill="var(--icon)"><use href="#i-more"/></svg><span>More</span></div>
  </nav>
</section>

<!-- PILOT DETAIL -->
<section class="screen" style="left:472px;top:1124px">
  <header class="hdr">
    <svg class="back" width="22" height="22" style="color:#222"><use href="#i-back"/></svg>
    <span class="sub">Pilot</span><span class="ttl">Avery, Clark, Blake</span>
    <span class="dots" style="left:378px;top:22px">···</span>
  </header>
  <div class="card" style="left:6px;top:63px;width:400px;height:349px"></div>
  <span style="left:28px;top:78px;font-size:12px;font-weight:500">Pilot</span>
  <span class="dots" style="left:376px;top:96px">···</span>
  <div class="tagrow" style="left:21px;top:101px">
    <span class="tag">Avery</span><span class="tag">Clark</span><span class="tag">Blake</span>
  </div>
  <div class="field" style="left:21px;top:148px;width:370px;height:49px"><span class="lbl">Pilot Certificate No.</span><svg class="ico" width="14" height="14" fill="var(--icon)"><use href="#i-check"/></svg><span class="val">3182133</span></div>
  <div class="field" style="left:21px;top:216px;width:370px;height:49px"><span class="lbl">Medical Expiration Date</span><svg class="ico" width="14" height="14" fill="var(--icon)"><use href="#i-cal"/></svg><span class="val">09/30/24</span></div>
  <div class="field" style="left:21px;top:284px;width:370px;height:49px"><span class="lbl">Flight Review Expiration Date</span><svg class="ico" width="14" height="14" fill="var(--icon)"><use href="#i-cal"/></svg><span class="val">06/30/24</span></div>
  <div class="field" style="left:21px;top:352px;width:370px;height:49px"><span class="lbl">Total Flight Time</span><svg class="ico" width="14" height="14" fill="var(--icon)"><use href="#i-takeoff"/></svg><span class="val">2500</span></div>

  <div class="card" style="left:6px;top:421px;width:400px;height:157px"></div>
  <svg width="14" height="14" fill="var(--icon)" style="left:21px;top:445px"><use href="#i-pin"/></svg>
  <span style="left:45px;top:434px;font-size:14px;line-height:18px;width:290px">X99, Pine Hollow Airfield, Pine Hollow, FL, 32000, 11, 2500</span>
  <i class="caret" style="left:354px;top:448px"></i>
  <div style="left:21px;top:480px;width:370px;height:1px;background:#e2e4e7"></div>
  <svg width="14" height="14" fill="var(--icon)" style="left:21px;top:505px"><use href="#i-pin"/></svg>
  <span style="left:45px;top:494px;font-size:14px;line-height:18px;width:290px">X99, Pine Hollow Airfield, Pine Hollow, FL, 32000, 11, 2500</span>
  <i class="caret" style="left:354px;top:508px"></i>
  <div style="left:21px;top:534px;width:370px;height:1px;background:#e2e4e7"></div>
  <svg width="16" height="16" style="left:21px;top:547px;color:var(--blue)"><use href="#i-plus"/></svg>
  <span class="link" style="left:48px;top:547px">Add Base Airport</span>

  <div class="card" style="left:6px;top:586px;width:400px;height:40px"></div>
  <svg width="18" height="18" fill="var(--blue)" style="left:20px;top:597px"><use href="#i-star"/></svg>
  <span class="link" style="left:48px;top:598px">Add Rating</span>

  <div class="card" style="left:6px;top:634px;width:400px;height:200px"></div>
  <div class="field" style="left:21px;top:655px;width:370px;height:49px"><span class="lbl">Emergency Contact</span><span class="val" style="left:16px">Rowan Avery</span><svg width="16" height="16" fill="var(--blue)" style="right:14px;top:16px"><use href="#i-phone"/></svg></div>
  <div class="field" style="left:21px;top:723px;width:370px;height:49px"><span class="lbl">Phone</span><svg class="ico" width="14" height="14" fill="var(--icon)"><use href="#i-phone"/></svg><span class="val">555-014-2287</span></div>
  <div class="field" style="left:21px;top:791px;width:370px;height:49px"><span class="lbl">Relationship</span><svg class="ico" width="14" height="14" fill="var(--icon)"><use href="#i-people"/></svg><span class="val">-</span></div>

  <nav class="tabs" style="top:835px">
    <div class="tab" style="left:11px"><svg width="28" height="28" fill="var(--icon)"><use href="#i-person"/></svg><span>Contact</span></div>
    <div class="tab on" style="left:89px"><svg width="28" height="28" fill="var(--blue)"><use href="#i-pilot"/></svg><span>Pilot</span></div>
    <div class="tab" style="left:167px"><svg width="28" height="28" fill="var(--icon)"><use href="#i-plane"/></svg><span>Plane</span></div>
    <div class="tab" style="left:245px"><svg width="28" height="28" fill="var(--icon)"><use href="#i-hand"/></svg><span>Flt Request</span></div>
    <div class="tab" style="left:323px"><svg width="28" height="28" fill="var(--icon)"><use href="#i-more"/></svg><span>More</span></div>
  </nav>
</section>

<!-- MORE MENU -->
<section class="screen" style="left:914px;top:1124px">
  <header class="hdr">
    <span class="solo">More</span>
    <span class="dots" style="left:378px;top:22px">···</span>
  </header>
  <div class="menu" style="top:63px"><svg width="22" height="22" fill="var(--icon)"><use href="#i-takeoff"/></svg><span>Flight</span></div>
  <div class="menu" style="top:121px"><svg width="22" height="22" fill="var(--icon)"><use href="#i-people"/></svg><span>Login</span></div>
  <div class="menu" style="top:179px"><svg width="22" height="22" fill="var(--icon)"><use href="#i-person"/></svg><span>Account</span></div>
  <div class="menu" style="top:237px"><svg width="22" height="22" fill="var(--icon)"><use href="#i-cal"/></svg><span>Calendar</span></div>
  <div class="menu" style="top:295px"><svg width="22" height="22" fill="var(--icon)"><use href="#i-users"/></svg><span>Users</span></div>
  <div class="menu" style="top:353px"><svg width="22" height="22" fill="var(--icon)"><use href="#i-home"/></svg><span>Dashboard</span></div>
  <div class="menu" style="top:411px"><svg width="22" height="22" fill="var(--icon)"><use href="#i-map"/></svg><span>Tracking</span></div>
  <div class="menu" style="top:469px"><svg width="22" height="22" fill="var(--icon)"><use href="#i-gift"/></svg><span>Outreach Event</span></div>
  <div class="menu" style="top:527px"><svg width="22" height="22" fill="var(--icon)"><use href="#i-wrench"/></svg><span>Maintenance Resource</span></div>
  <div class="menu" style="top:585px"><svg width="22" height="22" fill="var(--icon)"><use href="#i-gear"/></svg><span>Setting</span></div>

  <nav class="tabs" style="top:835px">
    <div class="tab" style="left:11px"><svg width="28" height="28" fill="var(--icon)"><use href="#i-person"/></svg><span>Contact</span></div>
    <div class="tab" style="left:89px"><svg width="28" height="28" fill="var(--icon)"><use href="#i-pilot"/></svg><span>Pilot</span></div>
    <div class="tab" style="left:167px"><svg width="28" height="28" fill="var(--icon)"><use href="#i-plane"/></svg><span>Plane</span></div>
    <div class="tab" style="left:245px"><svg width="28" height="28" fill="var(--icon)"><use href="#i-hand"/></svg><span>Flt Request</span></div>
    <div class="tab on" style="left:323px"><svg width="28" height="28" fill="var(--blue)"><use href="#i-more"/></svg><span>More</span></div>
  </nav>
</section>

</div>
</body>
</html>
```